Fast Growing Personal Injury Law Firm Needs Business Card Design

We need a business card design for a fast growing personal injury law firm in Florida. Our name is Darren Kolvisty, P.A. Our practice is comprised of younger attorneys (in their 30s) that employ more modern techniques/tools than our older competition. We would prefer a look that is a modern play on a classic look. Also, we would like to continue using a color scheme that employs navy blue and kelly green (other shades of green could be fine too) as well as our "E" logo.

Industry/Entity Type

Law Firm

```html
<!DOCTYPE html>
<html lang="en">
<head>
<meta charset="utf-8">
<title>Darren Kolvisty, P.A. — Business Card</title>
<link rel="stylesheet" href="https://fonts.googleapis.com/css2?family=Lato:wght@400;700;900&display=swap">
<style>
  :root {
    --green: #178a3c;
    --navy: #15306b;
    --navy-dark: #0f2456;
    --paper: #ffffff;
    --paper-shade: #eef0ef;
    --backdrop: #2b2b2b;
    --ink-on-green: #ffffff;
  }
  * { box-sizing: border-box; margin: 0; padding: 0; }
  html, body {
    width: 1200px; height: 873px; overflow: hidden;
    background: var(--backdrop);
    font-family: "Lato", Arial, sans-serif;
  }
  .canvas { position: relative; width: 1200px; height: 873px; }
  .card {
    position: absolute; width: 540px; height: 309px;
    background: linear-gradient(160deg, var(--paper) 40%, var(--paper-shade));
    overflow: hidden;
    box-shadow: 0 10px 30px rgba(0,0,0,.5);
  }
  .card--front { left: 40px; top: 110px; }
  .card--back { left: 620px; top: 454px; }
  .card__waves { position: absolute; inset: 0; width: 100%; height: 100%; }

  .lockup { position: absolute; display: flex; flex-direction: column; }
  .lockup__mark {
    width: 74px; height: 58px; background: var(--navy);
    border: 3px solid var(--paper); outline: 1px solid var(--navy);
    margin-bottom: 8px;
  }
  .lockup__name { color: var(--navy); font-weight: 900; font-size: 21px; line-height: 1.1; white-space: nowrap; }
  .lockup__tagline { color: var(--green); font-weight: 400; font-size: 18px; line-height: 1.2; white-space: nowrap; }

  .card--front .lockup { left: 56px; top: 74px; }
  .card--front .lockup__mark { margin-left: 22px; }
  .website {
    position: absolute; right: 30px; top: 150px;
    color: var(--ink-on-green); font-size: 12px; font-weight: 700;
    letter-spacing: 3px;
  }

  .card--back .lockup { right: 40px; top: 26px; align-items: flex-end; }
  .card--back .lockup__mark { margin-right: 66px; }
  .card--back .lockup__name { font-size: 19px; }
  .card--back .lockup__tagline { font-size: 17px; }

  .person { position: absolute; left: 44px; top: 168px; color: var(--ink-on-green); }
  .person__name { font-size: 19px; font-weight: 900; }
  .person__role { font-size: 14px; color: var(--navy-dark); margin-top: 3px; }
  .contacts { list-style: none; margin-top: 10px; }
  .contacts li { display: flex; align-items: center; gap: 10px; font-size: 13px; font-weight: 700; height: 23px; }
  .contacts svg { width: 15px; height: 15px; fill: none; stroke: var(--ink-on-green); stroke-width: 1.6; }
  .address {
    position: absolute; right: 40px; top: 236px; text-align: right;
    color: var(--ink-on-green); font-size: 13px; font-weight: 700; line-height: 1.45;
  }
</style>
</head>
<body>
<main class="canvas">

  <section class="card card--front" aria-label="Card front">
    <svg class="card__waves" viewBox="0 0 540 309" preserveAspectRatio="none" aria-hidden="true">
      <path d="M0,250 C150,262 262,238 320,172 C345,142 360,122 380,102 L380,140 C340,200 240,272 0,272 Z" fill="var(--navy)"/>
      <path d="M0,262 C150,272 270,250 330,170 C380,95 450,45 540,30 L540,309 L0,309 Z" fill="var(--green)"/>
    </svg>
    <div class="lockup">
      <div class="lockup__mark"></div>
      <div class="lockup__name">Darren Kolvisty, P.A.</div>
      <div class="lockup__tagline">Personal Injury Attorneys</div>
    </div>
    <div class="website">www.kolvistylaw.com</div>
  </section>

  <section class="card card--back" aria-label="Card back">
    <svg class="card__waves" viewBox="0 0 540 309" preserveAspectRatio="none" aria-hidden="true">
      <path d="M380,214 C460,212 520,160 540,100 L540,124 C512,190 455,226 380,214 Z" fill="var(--navy)"/>
      <path d="M0,150 C100,120 200,150 300,190 C380,222 470,222 540,122 L540,309 L0,309 Z" fill="var(--green)"/>
    </svg>
    <div class="lockup">
      <div class="lockup__mark"></div>
      <div class="lockup__name">Darren Kolvisty, P.A.</div>
      <div class="lockup__tagline">Personal Injury Attorneys</div>
    </div>
    <div class="person">
      <div class="person__name">Darren Kolvisty</div>
      <div class="person__role">Attorney at law</div>
      <ul class="contacts">
        <li><svg viewBox="0 0 16 16"><rect x="4" y="1" width="8" height="14" rx="1.5"/><line x1="7" y1="12.5" x2="9" y2="12.5"/></svg>941.555.0182</li>
        <li><svg viewBox="0 0 16 16"><rect x="4" y="1.5" width="8" height="4"/><rect x="1.5" y="5.5" width="13" height="6" rx="1"/><rect x="4" y="9.5" width="8" height="5"/></svg>941.555.0190</li>
        <li><svg viewBox="0 0 16 16"><rect x="1.5" y="3.5" width="13" height="9"/><polyline points="1.5,3.5 8,9 14.5,3.5"/></svg>darren@kolvistylaw.com</li>
      </ul>
    </div>
    <div class="address">2150 Harbor Point Drive Suite 210<br>Palmetto Bay, Florida 34100</div>
  </section>

</main>
</body>
</html>
```